Australian new start up company needs a Logo & Web Design

We need a smart, simple logo and web design for a new start up company based in Melbourne Australia called "Merchant Harbour Network". The logo is to be used on all marketing materials. The website is the primary interface of the company.

Our initial phase (launch) will provide a B2B directory service, resources and solutions.
A.) By listing on our site, small businesses can generate sales for their business. Regardless of where they might be located in the world, then can sell to Australian small businesses.
B.)Through our resource centre, small businesses can find practical and up to date resources for their business in pre-start up, start up, growth, maintenance and succession planning or exit stage.
C.)And on our site, we'll offer time and money saving solutions. These solutions can be packaged solutions (ie. Car Branding = including design, print and application onto the vehicle at a discounted price). Customers can also contact us if they want to advertise their business solution.

Eventually, there will be a total of five services inclusive of the directory described above (ie. business classifieds, link to Asian businesses, expos/seminars listing, etc). We hope to see this site grow over the next 18 months. All services will be aimed at servicing small businesses. Individuals through to large businesses located any where in the world can service these small businesses.

We would like to see designs that are professional. They should communicate growth, trust, professionalism and forward thinking.

Target Market(s)

Small Businesses (ie. employ up to 150 employees)

Industry/Entity Type

Business

Requirements
Must have
• We have attached some of the current files that we have designed ourselves. We feel that our material is lacking in appeal, professionalism and consistency. However, it does give a good idea of the requirements needed such as login, directory on the frontpage, etc. The wording is not final, as we are trying to finalise the design first. The logo was simply a placeholder as that definitely needs to be designed.

We want a logo and website that sticks in people's minds, its memorable.

We want a website that is EASY to use and navigate.
Nice to have
• Eventually, there will be a total of five services inclusive of the directory described above (ie. business classifieds, Asian businesses, expos/seminars listing, etc). They are very different types of services. The common thread is that all services will be aimed at servicing small businesses.

The winning design will need to help us to visualize how their design suits our future growth.

```html
<!DOCTYPE html>
<html lang="en">
<head>
<meta charset="utf-8">
<title>Merchant Harbour Network</title>
<link href="https://fonts.googleapis.com/css2?family=PT+Sans:wght@400;700&display=swap" rel="stylesheet">
<style>
:root{
  --purple:#8e2a8c;
  --purple-dark:#6e1c6c;
  --purple-light:#a23aa0;
  --green:#6cbb12;
  --green-dark:#4f9a08;
  --orange:#f39c12;
  --ink:#333;
  --muted:#666;
  --line:#ddd;
  --footer:#3a3a3a;
  --footer-low:#2b2b2b;
}
*{box-sizing:border-box;margin:0;padding:0}
html,body{width:772px;height:1200px;overflow:hidden;background:#fff}
body{position:relative;font-family:"PT Sans",Arial,sans-serif;color:var(--ink)}
.abs{position:absolute}

/* header */
.brand{left:46px;top:32px;font-size:24px;font-weight:700;color:var(--purple);letter-spacing:-.3px}
.login-box{left:483px;top:11px;width:246px;height:64px;border:1px solid #e4e4e4;box-shadow:0 0 3px rgba(0,0,0,.08);background:#fff}
.field{position:absolute;height:18px;border:1px solid #ccc;border-radius:3px;font-size:8px;color:#777;padding:3px 6px}
.login-box .user{left:13px;top:11px;width:106px}
.login-box .pass{left:126px;top:11px;width:106px}
.login-box .forgot{position:absolute;left:14px;top:35px;font-size:7.5px;color:#888}
.btn-sm{position:absolute;top:34px;height:16px;font-size:8px;color:#fff;text-align:center;line-height:16px;border-radius:2px}
.btn-post{left:132px;width:56px;background:var(--green)}
.btn-login{left:194px;width:38px;background:var(--orange)}

/* hero */
.hero{left:0;top:83px;width:772px;height:258px;background:linear-gradient(180deg,var(--purple-light),var(--purple-dark))}
.hero h1{position:absolute;left:52px;top:34px;font-weight:400;color:#fff;font-size:25px;line-height:1.05;letter-spacing:-.2px}
.hero h1 span{display:block;font-size:19px;margin-top:3px}
.hero ul{position:absolute;left:55px;top:93px;list-style:none;color:#fff;font-size:12px}
.hero li{height:21px;display:flex;align-items:center;gap:6px}
.dots{position:absolute;left:53px;top:195px;display:flex;gap:3px}
.dots i{width:7px;height:7px;border-radius:50%;background:#e6cfe6}
.preview{left:388px;top:112px;width:341px;height:229px;background:#fff;padding:6px 6px 0}
.preview div{width:100%;height:100%;background:linear-gradient(180deg,#e9ddb8 0%,#f6efd9 20%,#2f6db8 22%,#6aa2d6 48%,#f7f3e6 50%,#f7f3e6 100%)}

/* search */
.search{left:0;top:341px;width:772px;height:61px;background:linear-gradient(180deg,#e6e6e6,#f7f7f7)}
.search .lbl{position:absolute;top:20px;font-size:16px;color:#444}
.search .inp{position:absolute;top:20px;height:25px;background:#fff;border:1px solid #ccc;font-size:9px;color:#666;padding:6px 8px}
.find{position:absolute;left:617px;top:20px;width:55px;height:25px;background:#3a3a3a;color:#fff;font-size:12px;text-align:center;line-height:25px}

/* categories */
.section-title{left:52px;top:434px;font-size:20px;font-weight:400;color:#333}
.col{list-style:none;font-size:9.5px;color:#333}
.col li{height:17.5px;display:flex;align-items:center;gap:6px}
.plus{width:11px;height:11px;border:1px solid #bbb;border-radius:50%;position:relative;flex:none}
.plus::before,.plus::after{content:"";position:absolute;background:#999;left:50%;top:50%;transform:translate(-50%,-50%)}
.plus::before{width:5px;height:1px}.plus::after{width:1px;height:5px}
.col .active{color:var(--purple);padding-left:16px}
.sub{list-style:none;font-size:9px;color:#666;padding-left:29px}
.sub li{height:14.1px;display:flex;align-items:center;gap:6px}
.sub li::before{content:"";border-left:3px solid #aaa;border-top:2.5px solid transparent;border-bottom:2.5px solid transparent}
.divider{top:478px;width:1px;height:312px;background:var(--line)}
.resource{left:513px;top:762px;width:162px;height:29px;background:linear-gradient(180deg,var(--green),var(--green-dark));color:#fff;font-size:13px;text-align:center;line-height:29px}

/* packages */
.pkg{top:833px;width:157px;height:132px;background:linear-gradient(180deg,var(--purple-light),var(--purple-dark));color:#fff;box-shadow:0 8px 8px -6px rgba(0,0,0,.25)}
.pkg h3{position:absolute;left:18px;top:15px;font-weight:400;font-size:15px;line-height:1.1}
.pkg ul{position:absolute;left:19px;top:60px;list-style:none;font-size:8px}
.pkg li{height:14px;display:flex;align-items:center;gap:5px}
.pkg li::before{content:"";border-left:3px solid #fff;border-top:2.5px solid transparent;border-bottom:2.5px solid transparent}
.pkg svg{position:absolute;right:10px;bottom:12px}

/* footer */
.footer{left:0;top:1084px;width:772px;height:71px;background:var(--footer)}
.flinks{position:absolute;top:20px;list-style:none;font-size:9.5px;color:#fff}
.flinks li{height:17.5px;display:flex;align-items:center;gap:6px}
.flinks li::before{content:"";border-left:3px solid #999;border-top:3px solid transparent;border-bottom:3px solid transparent}
.social{position:absolute;left:647px;top:20px;display:flex;gap:4px}
.social i{width:18px;height:18px;border-radius:3px;background:#4a8fd0}
.social i:nth-child(2){background:#2f78b3}.social i:nth-child(3){background:#3b5ea6}
.copy{left:0;top:1155px;width:772px;height:45px;background:var(--footer-low);color:#bbb;font-size:7.5px;padding:17px 0 0 55px}
</style>
</head>
<body>

<div class="abs brand">Merchant Harbour Network</div>
<div class="abs login-box">
  <div class="field user">username</div>
  <div class="field pass">password</div>
  <div class="forgot">Forgotten your login details?</div>
  <div class="btn-sm btn-post">Post an ad</div>
  <div class="btn-sm btn-login">Login</div>
</div>

<section class="abs hero">
  <h1>Online directory, dedicated to<span>servicing Australian Small Businesses</span></h1>
  <ul>
    <li><svg width="13" height="10" viewBox="0 0 13 10"><path d="M1 5l4 4 7-8" stroke="#fff" stroke-width="2.4" fill="none"/></svg>Advertise for as little as $2/month</li>
    <li><svg width="13" height="10" viewBox="0 0 13 10"><path d="M1 5l4 4 7-8" stroke="#fff" stroke-width="2.4" fill="none"/></svg>Generate sales, increase brand awareness</li>
    <li><svg width="13" height="10" viewBox="0 0 13 10"><path d="M1 5l4 4 7-8" stroke="#fff" stroke-width="2.4" fill="none"/></svg>Limited time business offers</li>
    <li><svg width="13" height="10" viewBox="0 0 13 10"><path d="M1 5l4 4 7-8" stroke="#fff" stroke-width="2.4" fill="none"/></svg>Small Business resource centre</li>
  </ul>
  <div class="dots"><i></i><i></i><i></i></div>
</section>
<div class="abs preview"><div role="img" aria-label="Screenshot of a featured member website"></div></div>

<section class="abs search">
  <span class="lbl" style="left:84px">I need</span>
  <div class="inp" style="left:132px;width:243px">[enter your search requirement]</div>
  <span class="lbl" style="left:391px">located</span>
  <div class="inp" style="left:451px;width:158px">(enter postcode)</div>
  <div class="find">Find</div>
</section>

<h2 class="abs section-title">Browse by Categories</h2>

<ul class="abs col" style="left:72px;top:473px">
  <li><span class="plus"></span>Accounting</li>
  <li class="active">+ Artwork Design</li>
</ul>
<ul class="abs sub" style="left:72px;top:512px">
  <li>Banner</li><li>Blog</li><li>Brochure</li><li>Electronic Stationery</li><li>Templates</li><li>Social Page</li><li>Flyer</li><li>Logo</li><li>Slide Deck</li><li>Restaurant Menu</li><li>Stationery</li><li>Sticker</li><li>T-Shirt</li><li>Micro Blog</li><li>Vehicle Signage</li><li>Website Design</li>
</ul>
<ul class="abs col" style="left:72px;top:741px">
  <li><span class="plus"></span>Banking &amp; Finance</li>
  <li><span class="plus"></span>Category</li>
  <li><span class="plus"></span>Category</li>
</ul>

<div class="abs divider" style="left:230px"></div>
<ul class="abs col" style="left:277px;top:473px">
  <li><span class="plus"></span>Bookkeeping</li><li><span class="plus"></span>Capital Raising</li><li><span class="plus"></span>Cleaning Services &amp; Suppliers</li><li><span class="plus"></span>Coaching/Training</li><li><span class="plus"></span>Courier Service</li><li><span class="plus"></span>Equipment Hire</li><li><span class="plus"></span>Event planning &amp; Coordination</li><li><span class="plus"></span>Facilities</li><li><span class="plus"></span>Fitness</li><li><span class="plus"></span>Information Technology</li><li><span class="plus"></span>Insurance</li><li><span class="plus"></span>Legal Advice</li><li><span class="plus"></span>Manufacturing</li><li><span class="plus"></span>Marking &amp; Public Relations</li><li><span class="plus"></span>Payroll Services</li><li><span class="plus"></span>Category</li><li><span class="plus"></span>Category</li><li><span class="plus"></span>Category</li>
</ul>

<div class="abs divider" style="left:470px"></div>
<ul class="abs col" style="left:511px;top:472px">
  <li><span class="plus"></span>Photography/Videography</li><li><span class="plus"></span>Printing</li><li><span class="plus"></span>Promotional Materials</li><li><span class="plus"></span>Recruitment</li><li><span class="plus"></span>Sales</li><li><span class="plus"></span>Sewing &amp; Tailoring</li><li><span class="plus"></span>Shop Fit Outs &amp; Equipment</li><li><span class="plus"></span>Signage</li><li><span class="plus"></span>Stationery</li><li><span class="plus"></span>Superannuation</li><li><span class="plus"></span>Tradesman</li><li><span class="plus"></span>Translation Service</li><li><span class="plus"></span>Travel Service</li><li><span class="plus"></span>Uniforms/Corporate Wear</li><li><span class="plus"></span>Repair &amp; Maintenance</li><li><span class="plus"></span>Virtual Assistants</li>
</ul>
<div class="abs resource">Resource Center</div>

<div class="abs pkg" style="left:54px"><h3>Start-Up Package<br>$2000</h3><ul><li>Logo Design</li><li>Website Design</li><li>Stationery</li><li>Directory Listing</li></ul><svg width="46" height="46" viewBox="0 0 46 46"><path d="M46 0V46H0Z" fill="#fff"/><text x="24" y="38" font-size="15" fill="#555" font-family="PT Sans,sans-serif">go</text></svg></div>
<div class="abs pkg" style="left:223px"><h3>Biz Growth Package<br>$1000</h3><ul><li>Logo Design</li><li>Website Design</li><li>Stationery</li><li>Directory Listing</li></ul><svg width="46" height="46" viewBox="0 0 46 46"><path d="M46 0V46H0Z" fill="#fff"/><text x="24" y="38" font-size="15" fill="#555" font-family="PT Sans,sans-serif">go</text></svg></div>
<div class="abs pkg" style="left:391px"><h3>Biz Coaching<br>$2500</h3><ul><li>xx hours of</li><li>Business Coaching</li><li>Directory Listing</li></ul><svg width="46" height="46" viewBox="0 0 46 46"><path d="M46 0V46H0Z" fill="#fff"/><text x="24" y="38" font-size="15" fill="#555" font-family="PT Sans,sans-serif">go</text></svg></div>
<div class="abs pkg" style="left:560px"><h3>Vehicle Advertising<br>$3000</h3><ul><li>Artwork Printing</li><li>Vehicle Placement</li><li>Directory Listing</li></ul><svg width="46" height="46" viewBox="0 0 46 46"><path d="M46 0V46H0Z" fill="#fff"/><text x="24" y="38" font-size="15" fill="#555" font-family="PT Sans,sans-serif">go</text></svg></div>

<ul class="abs col" style="left:73px;top:1004px"><li><span class="plus"></span>Category 1</li><li><span class="plus"></span>Category 2</li><li><span class="plus"></span>Category 3</li></ul>
<ul class="abs col" style="left:277px;top:1004px"><li><span class="plus"></span>Category 4</li><li><span class="plus"></span>Category 5</li><li><span class="plus"></span>Category 6</li></ul>
<ul class="abs col" style="left:511px;top:1004px"><li><span class="plus"></span>Category 7</li><li><span class="plus"></span>Category 8</li><li><span class="plus"></span>Category 9</li></ul>

<footer class="abs footer">
  <ul class="flinks" style="left:74px"><li>How it works</li><li>Post an Ad</li></ul>
  <ul class="flinks" style="left:183px"><li>Login</li><li>Contact Us</li></ul>
  <ul class="flinks" style="left:280px"><li>Resource Centre</li><li>Asia Link</li></ul>
  <ul class="flinks" style="left:394px"><li>Terms &amp; Conditions</li><li>Privacy</li></ul>
  <div class="social"><i></i><i></i><i></i></div>
</footer>
<div class="abs copy">© Merchant Harbour Network Group 2012. Use of this website constitutes acceptance of our Terms and Conditions and Privacy</div>

</body>
</html>
```